design a construction company business card

Design business card around our logo. Card must have all the typical info: name, title, address, phone, email, business name, etc. Somewhere on the card I would like to see our motto "Built on integrity... Inspired by commitment." Consider adding a splash of bright orange to the card to complement the blues and silvers/grays in the logo. We are open to metallic inks, textures, etc. We would like to see options on both light and dark backgrounds. The font in the logo is Euro Technic Extended Regular.

```html
<!DOCTYPE html>
<html lang="en">
<head>
<meta charset="utf-8">
<title>Business Card – Front and Back</title>
<link rel="stylesheet" href="https://fonts.googleapis.com/css2?family=Open+Sans:wght@400;600;700&display=swap">
<style>
  :root {
    --stage-center: #e9eaeb;
    --stage-edge: #cdcecf;
    --blue-deep: #2b3990;
    --blue-bright: #1c75bc;
    --curve-gray: #8a8c8f;
    --white: #ffffff;
    --card-dark: #231f20;
    --brand-blue: #2448a8;
  }
  * { margin: 0; padding: 0; box-sizing: border-box; }
  html, body { width: 800px; height: 1200px; overflow: hidden; }
  body {
    position: relative;
    font-family: "Open Sans", Arial, sans-serif;
    background: radial-gradient(ellipse at 50% 50%, var(--stage-center) 0%, var(--stage-edge) 100%);
  }
  .card {
    position: absolute;
    left: 148px;
    width: 504px;
    height: 288px;
    overflow: hidden;
  }
  .card-front {
    top: 164px;
    border-radius: 16px;
    background: var(--white);
  }
  .card-back {
    top: 704px;
    background: var(--card-dark);
  }
  .front-shape { position: absolute; inset: 0; width: 504px; height: 288px; }
  .contact-block { position: absolute; left: 16px; top: 0; color: var(--white); }
  .person-name {
    position: absolute; top: 46px; left: 0;
    font-size: 21px; font-weight: 700; white-space: nowrap; letter-spacing: -0.2px;
  }
  .person-title {
    position: absolute; top: 74px; left: 1px;
    font-size: 12.8px; white-space: nowrap;
  }
  .address {
    position: absolute; top: 113px; left: 1px;
    font-size: 12.4px; line-height: 17px; white-space: nowrap;
  }
  .contact-list { position: absolute; top: 174px; left: 1px; list-style: none; }
  .contact-list li {
    display: flex; align-items: center; height: 18.5px;
    font-size: 12.4px; white-space: nowrap;
  }
  .contact-list svg { width: 9px; height: 9px; margin-right: 6px; fill: var(--white); }
  .brand {
    position: absolute; display: flex; align-items: center; gap: 6px;
    font-weight: 700; white-space: nowrap;
    transform: translate(-50%, -50%);
  }
  .brand-front {
    left: 389px; top: 156px; font-size: 14px; color: var(--brand-blue);
  }
  .brand-back {
    left: 50%; top: 50%; font-size: 15px; color: var(--white);
  }
  .brand-mark { width: 10px; height: 10px; background: currentColor; }
</style>
</head>
<body>
  <section class="card card-front">
    <svg class="front-shape" viewBox="0 0 630 360" aria-hidden="true">
      <defs>
        <linearGradient id="panelBlue" x1="0" y1="0" x2="1" y2="0">
          <stop offset="0" stop-color="#2b3990"/>
          <stop offset="1" stop-color="#1c75bc"/>
        </linearGradient>
      </defs>
      <path d="M268 0 C 235 40, 225 110, 265 175 C 300 230, 335 255, 330 300 C 325 330, 310 345, 295 360 L312 360 C 328 345, 340 325, 338 295 C 335 255, 300 225, 270 170 C 240 110, 245 45, 276 0 Z" fill="#8a8c8f"/>
      <path d="M0 0 H268 C 235 40, 225 110, 265 175 C 300 230, 335 255, 330 300 C 325 330, 310 345, 295 360 H0 Z" fill="url(#panelBlue)"/>
    </svg>
    <div class="contact-block">
      <h1 class="person-name">Daniel Marsh</h1>
      <p class="person-title">Managing Member</p>
      <p class="address">2750 Foundry Lane,<br>Riverton, CA 95640</p>
      <ul class="contact-list">
        <li><svg viewBox="0 0 10 10"><path d="M2 1 L4 3 L3 4 C4 6 4 6 6 7 L7 6 L9 8 L7.5 9.5 C4 9 1 6 0.5 2.5 Z"/></svg>(916) 555-0142</li>
        <li><svg viewBox="0 0 10 10"><path d="M2.5 0 H7.5 V10 H2.5 Z M3.5 1 V8 H6.5 V1 Z" fill-rule="evenodd"/></svg>(530) 555-0187</li>
        <li><svg viewBox="0 0 10 10"><path d="M0 2 H10 V8.5 H0 Z M0.8 2.8 L5 5.8 L9.2 2.8 Z" fill-rule="evenodd"/></svg>daniel@haldenbuild.com</li>
        <li><svg viewBox="0 0 10 10"><circle cx="5" cy="5" r="4.5"/></svg>www.haldenbuild.com</li>
      </ul>
    </div>
    <div class="brand brand-front"><span class="brand-mark"></span>HALDEN BUILDERS, INC.</div>
  </section>

  <section class="card card-back">
    <div class="brand brand-back"><span class="brand-mark"></span>HALDEN BUILDERS, INC.</div>
  </section>
</body>
</html>
```